Brellwick Finance Stationary Design

We have selected a logo as our winner, we now need a full stationary set to be in the same theme.
Required:
- Letter Head
- Business Card Template
- Custom Envelopes
- A5 Notepad Design (Front cover and content pages. Content pages blank(no lines) but with our branding on them,)
- With Compliments Slip
Updates

Hey All,

We have changed the colour scheme of our logo. Our apologies if anyone has begun designing based off the old scheme. Please see the updated scheme in the brief,

Tobin

Target Market(s)

Target market is experienced property developers and financial institutions.

Industry/Entity Type

Commercial Finance

Font styles to use
Serif

Colors
0054AA
0677BA
7BADD7
CADEEF
E8F1F8
0094D4
00A9DD
6FCCEA
C7EBF8
E9F6FB
00AB8E
00BBA5
67D7C9
C6EFE9
E9F9F6
59FF00
82FF00
B8FF75
E3FFCB
F4FFEA

```html
<!DOCTYPE html>
<html lang="en">
<head>
<meta charset="utf-8">
<title>Brellwick Finance Stationery Set</title>
<link rel="stylesheet" href="https://fonts.googleapis.com/css2?family=Montserrat:wght@600;700;800&display=swap">
<style>
  :root {
    --backdrop: #9cb1bc;
    --paper: #ffffff;
    --paper-shade: #eef0f3;
    --brand-blue: #0036a3;
    --brand-blue-deep: #0a2a8a;
    --brand-green: #23843b;
    --cover-mist: #9eb2bd;
    --rule-grey: #9a9a9a;
    --rule-dark: #333333;
    --window: #d9dcdf;
    --divider: #e4e6e8;
  }
  html, body {
    margin: 0;
    padding: 0;
    width: 1200px;
    height: 1000px;
    overflow: hidden;
    background: var(--backdrop);
  }
  .stationery-board { display: block; width: 1200px; height: 1000px; }
  .sheet { fill: var(--paper); }
  .sheet-shade { fill: var(--paper-shade); }
  .band-blue { fill: var(--brand-blue); }
  .band-blue-deep { fill: var(--brand-blue-deep); }
  .band-green { fill: var(--brand-green); }
  .cover-mist { fill: var(--cover-mist); }
  .rule { stroke: var(--rule-grey); stroke-width: 2.4; }
  .rule-dark { stroke: var(--rule-dark); stroke-width: 2.4; }
  .contact-icon { fill: var(--rule-dark); }
  .card-divider { stroke: var(--divider); stroke-width: 2; }
  .envelope-window { fill: var(--window); stroke: #b8bcc0; stroke-width: 1; }
  .brand-name {
    font-family: "Montserrat", sans-serif;
    font-weight: 800;
    fill: var(--brand-blue);
    letter-spacing: 0.02em;
  }
  .brand-name--light { fill: var(--paper); }
  .subject-title {
    font-family: "Montserrat", sans-serif;
    font-weight: 700;
    font-size: 9px;
    fill: var(--rule-dark);
    letter-spacing: 0.04em;
  }
  .card-name {
    font-family: "Montserrat", sans-serif;
    font-weight: 700;
    font-size: 11.5px;
    fill: var(--rule-dark);
    letter-spacing: 0.04em;
  }
  .card-role {
    font-family: "Montserrat", sans-serif;
    font-weight: 700;
    font-size: 6.5px;
    fill: var(--rule-dark);
  }
</style>
</head>
<body>
<svg class="stationery-board" viewBox="0 0 1200 1000" xmlns="http://www.w3.org/2000/svg">

  <!-- Letterhead -->
  <g class="letterhead">
    <rect class="sheet" x="261" y="97" width="283" height="377"/>
    <rect class="sheet-shade" x="261" y="222" width="283" height="127"/>
    <text class="brand-name" x="341" y="170" font-size="9" text-anchor="middle">BRELLWICK FINANCE</text>
    <g transform="translate(447,152)">
      <rect class="contact-icon" x="0" y="-2" width="6" height="4" rx="1"/>
      <circle class="contact-icon" cx="3" cy="10" r="2.5"/>
      <circle class="contact-icon" cx="3" cy="23" r="2"/>
      <line class="rule-dark" x1="10" y1="0" x2="68" y2="0"/>
      <line class="rule-dark" x1="10" y1="9" x2="47" y2="9"/>
      <line class="rule-dark" x1="10" y1="13" x2="68" y2="13"/>
      <line class="rule-dark" x1="10" y1="22" x2="62" y2="22"/>
    </g>
    <text class="subject-title" x="295" y="240">Subject Title Space Here</text>
    <g class="letter-body">
      <line class="rule" x1="305" y1="255" x2="513" y2="255"/>
      <line class="rule" x1="295" y1="262" x2="513" y2="262"/>
      <line class="rule" x1="295" y1="269" x2="513" y2="269"/>
      <line class="rule" x1="295" y1="276" x2="513" y2="276"/>
      <line class="rule" x1="295" y1="283" x2="513" y2="283"/>
      <line class="rule" x1="295" y1="290" x2="325" y2="290"/>
      <line class="rule" x1="295" y1="307" x2="513" y2="307"/>
      <line class="rule" x1="295" y1="314" x2="513" y2="314"/>
      <line class="rule" x1="295" y1="321" x2="513" y2="321"/>
      <line class="rule" x1="295" y1="328" x2="370" y2="328"/>
      <line class="rule" x1="295" y1="345" x2="513" y2="345"/>
      <line class="rule" x1="295" y1="352" x2="513" y2="352"/>
      <line class="rule" x1="295" y1="359" x2="513" y2="359"/>
      <line class="rule" x1="295" y1="366" x2="342" y2="366"/>
      <line class="rule" x1="453" y1="393" x2="513" y2="393"/>
      <line class="rule-dark" x1="398" y1="400" x2="513" y2="400"/>
      <line class="rule" x1="444" y1="407" x2="513" y2="407"/>
    </g>
    <polygon class="band-green" points="395,452 544,452 544,467 410,467"/>
    <polygon class="band-blue" points="261,445 386,445 415,474 261,474"/>
  </g>

  <!-- Notepad cover -->
  <g class="notepad-cover">
    <rect class="sheet" x="658" y="73" width="307" height="408"/>
    <path class="cover-mist" d="M658 300 L965 258 L965 393 Q860 440 740 434 Q690 432 658 428 Z"/>
    <path class="band-blue" d="M658 73 H965 V258 L658 300 Z"/>
    <text class="brand-name brand-name--light" x="811" y="175" font-size="11" text-anchor="middle">BRELLWICK FINANCE</text>
    <polygon class="band-green" points="805,466 965,466 965,477 815,477"/>
    <polygon class="band-blue" points="661,462 798,462 826,481 661,481"/>
  </g>

  <!-- Envelope back -->
  <g class="envelope-back">
    <rect class="sheet" x="239" y="545" width="327" height="169"/>
    <path class="band-green" d="M239 545 L254 512 Q260 500 275 500 H530 Q545 500 551 512 L566 545 Z"/>
    <path class="band-blue-deep" d="M239 545 H566 L556 582 Q548 594 525 595 H285 Q258 594 248 578 Z"/>
    <path class="band-blue" d="M239 545 H566 L556 577 Q548 587 525 588 H285 Q258 588 248 574 Z"/>
  </g>

  <!-- Business card front -->
  <g class="business-card-front">
    <rect class="sheet" x="658" y="567" width="277" height="158"/>
    <text class="brand-name" x="799" y="636" font-size="8.5" text-anchor="middle">BRELLWICK FINANCE</text>
    <polygon class="band-green" points="790,711 935,711 935,720 800,720"/>
    <polygon class="band-blue" points="658,707 782,707 808,725 658,725"/>
  </g>

  <!-- Envelope front -->
  <g class="envelope-front">
    <rect class="sheet" x="239" y="763" width="327" height="169"/>
    <text class="brand-name" x="304" y="806" font-size="8.5" text-anchor="middle">BRELLWICK FINANCE</text>
    <g transform="translate(260,879)">
      <rect class="contact-icon" x="0" y="-2" width="6" height="4" rx="1"/>
      <circle class="contact-icon" cx="3" cy="8" r="2"/>
      <circle class="contact-icon" cx="3" cy="18" r="1.8"/>
      <line class="rule-dark" x1="10" y1="0" x2="61" y2="0"/>
      <line class="rule-dark" x1="10" y1="7" x2="42" y2="7"/>
      <line class="rule-dark" x1="10" y1="11" x2="61" y2="11"/>
      <line class="rule-dark" x1="10" y1="18" x2="55" y2="18"/>
    </g>
    <rect class="envelope-window" x="394" y="846" width="143" height="64" rx="5"/>
    <polygon class="band-green" points="390,916 566,916 566,927 402,927"/>
    <polygon class="band-blue" points="239,911 386,911 417,932 239,932"/>
  </g>

  <!-- Business card back -->
  <g class="business-card-back">
    <rect class="sheet" x="658" y="766" width="277" height="159"/>
    <text class="brand-name" x="722" y="846" font-size="8.5" text-anchor="middle">BRELLWICK FINANCE</text>
    <line class="card-divider" x1="789" y1="800" x2="789" y2="890"/>
    <text class="card-name" x="803" y="815">Name Surname</text>
    <text class="card-role" x="803" y="823">Business Title</text>
    <g transform="translate(805,836)">
      <rect class="contact-icon" x="0" y="-2" width="6" height="4" rx="1"/>
      <circle class="contact-icon" cx="3" cy="12" r="2.4"/>
      <circle class="contact-icon" cx="3" cy="28" r="2"/>
      <line class="rule-dark" x1="12" y1="0" x2="84" y2="0"/>
      <line class="rule-dark" x1="12" y1="11" x2="58" y2="11"/>
      <line class="rule-dark" x1="12" y1="15" x2="84" y2="15"/>
      <line class="rule-dark" x1="12" y1="26" x2="76" y2="26"/>
      <line class="rule-dark" x1="12" y1="30" x2="76" y2="30"/>
    </g>
    <polygon class="band-green" points="790,912 935,912 935,921 800,921"/>
    <polygon class="band-blue" points="658,907 782,907 808,925 658,925"/>
  </g>
</svg>
</body>
</html>
```